Blog Header Design for Programming Site

I am about to setup a blog using Typepad and I would like a custom graphic design to give my website that much needed unique look. The blog (to be called Marcus & Derek) is largely about programming, especially artificial intelligence. Books reviews might be included from time to time. This is not a business, but a personal website meant to display our programming skill sets.
Updates

We have gotten 2 designs from 2 different designers that we are pretty fond of.  Just in case, I want people to know that it should not be restricted to simply showing our faces.  You could have us with bodies doing something.  As an example, one holding a laptop and the other holding a Zelkor's cube or something.  We want our faces somewhere, but it doesn't have to be just faces.

Target Market(s)

Anyone interested in programming or potential employers.

Industry/Entity Type

Software

Requirements
Must have
• Graphic versions of our faces. Included are some JPGs. Marcus 1, Marcus 2 and Marcus 3 is of course Marcus while Wenbo 1 and Wenbo 2 are Derek. They do not have to be super detailed. Not exactly sure what we want in terms of how our faces should be used. It could be easily be "Marcus & Derek" in the middle with Marcus leaning on the word Marcus doing something and Derek leaning on the word Derek doing something. This is totally up to you.
Nice to have
• Even though the subject matter is sort of nerdy, we are probably wanting to go for an edgy look, sort of like something you expect see on blogs that deal with games.
Should not have
• Let your creative juices go. Should simply not have a nerdy look to it. Last time I requested a design, some people submitted some designs using bright colors that made it look really childish.

```html
<!DOCTYPE html>
<html lang="en">
<head>
<meta charset="utf-8">
<title>Marcus + Derek — Blog Header</title>
<link rel="stylesheet" href="https://fonts.googleapis.com/css2?family=Arimo:wght@400;700&display=swap">
<style>
  :root {
    --sky-light: #4b90ca;
    --sky-deep: #4068ac;
    --code-ink: rgba(20, 40, 80, 0.2);
    --title-ink: #0a0a0a;
    --accent-orange: #f4a12c;
    --accent-edge: #1a1a1a;
    --portrait-dark: #2e4f8a;
    --portrait-mid: #6d8fbf;
  }
  html, body {
    margin: 0;
    padding: 0;
    overflow: hidden;
    background: #ffffff;
  }
  .header-banner {
    position: relative;
    width: 1200px;
    height: 300px;
    overflow: hidden;
    background: var(--sky-light);
    font-family: "Arimo", Arial, sans-serif;
  }
  .backdrop {
    position: absolute;
    inset: 0;
  }
  .code-backdrop {
    position: absolute;
    left: 524px;
    top: 4px;
    margin: 0;
    font-family: "Arimo", Arial, sans-serif;
    font-size: 21px;
    line-height: 22.5px;
    color: var(--code-ink);
    white-space: pre;
  }
  .portraits {
    position: absolute;
    left: 0;
    top: 0;
    width: 510px;
    height: 300px;
  }
  .brace {
    position: absolute;
    left: 514px;
    margin: 0;
    font-weight: 700;
    font-size: 74px;
    line-height: 1;
    color: var(--title-ink);
  }
  .brace-open { top: 38px; }
  .brace-close { top: 196px; }
  .blog-title {
    position: absolute;
    left: 530px;
    top: 96px;
    margin: 0;
    font-weight: 700;
    font-size: 84px;
    line-height: 1;
    letter-spacing: 0;
    white-space: nowrap;
    color: var(--title-ink);
  }
  .accent-square {
    position: absolute;
    left: 1110px;
    top: 210px;
    width: 54px;
    height: 54px;
    box-sizing: border-box;
    background: var(--accent-orange);
    border: 3px solid var(--accent-edge);
  }
</style>
</head>
<body>
  <header class="header-banner">
    <svg class="backdrop" width="1200" height="300" viewBox="0 0 1200 300" aria-hidden="true">
      <rect width="1200" height="300" fill="var(--sky-light)"/>
      <polygon points="0,0 320,0 1200,140 1200,300 0,300" fill="var(--sky-deep)"/>
    </svg>

    <pre class="code-backdrop" aria-hidden="true">float Score(const Node * node) {
bool Search(Node * root, int goal) {
queue&lt;Node*&gt; open;
open.push(root);
while (!open.empty()) {
Node * cur = open.front();
open.pop();
if (cur-&gt;value == goal)
return true;
for (Node * kid : cur-&gt;kids)
open.push(kid);
return false;</pre>

    <svg class="portraits" viewBox="0 0 510 300" role="img" aria-label="Illustrated portraits of Marcus, in a cap and sunglasses, and Derek, in glasses and a black shirt">
      <defs>
        <linearGradient id="portrait-tone" x1="0" y1="0" x2="0" y2="1">
          <stop offset="0" stop-color="var(--portrait-mid)"/>
          <stop offset="1" stop-color="var(--portrait-dark)"/>
        </linearGradient>
      </defs>
      <path d="M40 300 C40 230 60 200 70 160 C60 90 90 20 160 20 C220 20 250 60 260 110 C280 50 330 20 380 30 C450 45 470 110 450 170 C440 210 460 240 480 300 Z" fill="url(#portrait-tone)"/>
    </svg>

    <p class="brace brace-open" aria-hidden="true">{</p>
    <h1 class="blog-title">Marcus + Derek</h1>
    <p class="brace brace-close" aria-hidden="true">}</p>
    <div class="accent-square" aria-hidden="true"></div>
  </header>
</body>
</html>
```